Design new marketing postcard for mortgage loan applicants

I have provided a postcard recently designed as a possible guide for this project and have attached it. The new text is rough drafted and included. Please feel free to design outside of the old postcard or you can design close to it.

```html
<!DOCTYPE html>
<html lang="en">
<head>
<meta charset="utf-8">
<title>Harborline Lending Postcard</title>
<link href="https://fonts.googleapis.com/css2?family=Oswald:wght@600&family=Lato:ital,wght@0,400;0,700;0,900;1,400;1,700&display=swap" rel="stylesheet">
<style>
:root{
  --bg:#5f5f5f;
  --navy:#0f3556;
  --navy-deep:#0a2744;
  --navy-light:#1c5683;
  --red:#e0252c;
  --red-deep:#b91f26;
  --gold:#b47a2e;
  --gold-dot:#e1a93a;
  --gold-text:#f0c453;
  --white:#ffffff;
  --paper:#fbfaf6;
  --ink:#1b1b1b;
  --line:#bdbdbd;
  --divider:#cfcfcf;
}
*{margin:0;padding:0;box-sizing:border-box}
html,body{width:902px;height:1200px;overflow:hidden}
body{background:var(--bg);position:relative;font-family:'Lato',sans-serif}
.card{position:absolute;width:854px;height:581px;background:var(--white);overflow:hidden;transform:scale(.902);transform-origin:0 0}
.card-front{left:42px;top:50px}
.card-back{left:87px;top:603px}
.card svg.shapes{position:absolute;left:0;top:0}
.abs{position:absolute}

.headline{left:408px;top:38px;font-family:'Oswald',sans-serif;font-weight:600;font-size:52px;color:var(--red);line-height:1;white-space:nowrap;letter-spacing:-.5px;transform:scaleX(.78);transform-origin:0 0}
.subhead{left:413px;top:104px;font-family:'Lato',sans-serif;font-weight:900;font-size:23px;color:var(--navy);line-height:1;white-space:nowrap}
.benefits{left:502px;top:160px;list-style:none}
.benefits li{font-style:italic;font-size:20px;color:var(--white);line-height:30.4px;padding-left:31px;position:relative;white-space:nowrap}
.benefits li::before{content:"";position:absolute;left:0;top:10px;width:11px;height:11px;border-radius:50%;background:var(--gold-dot)}

.brand{display:flex;align-items:center;gap:12px}
.brand-dot{width:34px;height:34px;border-radius:50%;background:var(--gold);flex:none}
.brand-name{font-weight:700;color:var(--navy);line-height:1.05;border-left:1px solid var(--divider);padding:14px 0 14px 12px;white-space:nowrap}
.front-brand{left:510px;top:334px}
.front-brand .brand-name{font-size:19px}
.nmls{left:638px;top:410px;font-size:16px;color:var(--ink)}

.call-row{display:flex;align-items:center;white-space:nowrap}
.call-tag{font-weight:700;line-height:1;display:flex;align-items:center;justify-content:center}
.front-call{left:118px;top:470px}
.front-call .call-tag{background:var(--red);color:var(--white);width:122px;height:51px;font-size:36px}
.front-call .phone{font-weight:900;font-size:68px;color:var(--white);margin-left:18px;letter-spacing:1px}

.back-brand{left:48px;top:40px}
.back-brand .brand-name{font-size:21px;padding:28px 0 28px 14px}
.message{left:43px;top:168px;width:383px;font-size:17px;color:var(--white);line-height:20.6px;text-align:justify;letter-spacing:.2px}
.invite{left:43px;top:264px;font-style:italic;font-weight:700;font-size:16px;color:var(--gold-text);line-height:20.5px;white-space:nowrap}
.fineprint{left:36px;top:336px;width:401px;font-size:11.2px;color:var(--ink);line-height:13.6px;text-align:justify}
.back-call{left:34px;top:497px}
.back-call .call-tag{background:var(--white);color:var(--navy);width:86px;height:38px;font-size:29px}
.back-call .phone{font-weight:900;font-size:43px;color:var(--white);margin-left:11px}
.stamp-box{left:682px;top:49px;width:127px;height:100px;border:1px solid var(--line)}
.address-line{left:565px;width:254px;height:1px;background:var(--line)}
</style>
</head>
<body>

<section class="card card-front">
  <svg class="shapes" width="854" height="581" viewBox="0 0 854 581">
    <defs>
      <linearGradient id="photoTone" x1="0" y1="0" x2="0" y2="1">
        <stop offset="0" stop-color="#5aa9dc"/>
        <stop offset=".45" stop-color="#8fd0e6"/>
        <stop offset=".7" stop-color="#d9c9b4"/>
        <stop offset="1" stop-color="#e8d8c2"/>
      </linearGradient>
      <linearGradient id="navyBand" x1="0" y1="0" x2="1" y2="0">
        <stop offset="0" stop-color="#0a2744"/>
        <stop offset=".6" stop-color="#1c5683"/>
        <stop offset="1" stop-color="#0f3556"/>
      </linearGradient>
      <linearGradient id="topWhite" x1="0" y1="0" x2="1" y2="0">
        <stop offset="0" stop-color="#e6e6e6"/>
        <stop offset=".5" stop-color="#ffffff"/>
      </linearGradient>
    </defs>
    <rect width="854" height="581" fill="url(#topWhite)"/>
    <rect x="440" y="148" width="414" height="177" fill="url(#navyBand)"/>
    <path d="M0,0 H318 C395,110 455,290 478,450 L0,460 Z" fill="url(#photoTone)" role="img" aria-label="Photo of a smiling couple on a sunny beach"/>
    <path d="M318,0 C395,110 455,290 478,450" fill="none" stroke="var(--gold)" stroke-width="9"/>
    <path d="M0,462 C260,430 560,424 854,470 V581 H0 Z" fill="var(--gold)"/>
    <path d="M0,478 C260,446 560,440 854,478 V581 H0 Z" fill="var(--white)"/>
    <path d="M0,488 C260,455 560,448 854,482 V581 H0 Z" fill="url(#navyBand)"/>
  </svg>

  <h1 class="abs headline">CASH OUT EQUITY LOAN</h1>
  <p class="abs subhead">ON YOUR INVESTMENT PROPERTY</p>
  <ul class="abs benefits">
    <li>Loan Based on your equity</li>
    <li>Fast close</li>
    <li>No Income Qualifying</li>
    <li>Not based on credit scores</li>
    <li>Competitive Rates</li>
  </ul>

  <div class="abs brand front-brand">
    <span class="brand-dot"></span>
    <span class="brand-name">Harborline Lending<br>Group, Inc.</span>
  </div>
  <p class="abs nmls">NMLS # 418207</p>

  <div class="abs call-row front-call">
    <span class="call-tag">CALL</span>
    <span class="phone">800-555-0147</span>
  </div>
</section>

<section class="card card-back">
  <svg class="shapes" width="854" height="581" viewBox="0 0 854 581">
    <defs>
      <clipPath id="panelClip">
        <path d="M0,0 H380 C470,150 520,380 592,581 H0 Z"/>
      </clipPath>
      <linearGradient id="navyBack" x1="0" y1="0" x2="1" y2="0">
        <stop offset="0" stop-color="#0a2744"/>
        <stop offset=".65" stop-color="#1c5683"/>
        <stop offset="1" stop-color="#0f3556"/>
      </linearGradient>
      <linearGradient id="redBack" x1="0" y1="0" x2="1" y2="0">
        <stop offset="0" stop-color="#b91f26"/>
        <stop offset="1" stop-color="#c9272d"/>
      </linearGradient>
    </defs>
    <path d="M0,0 H380 C470,150 520,380 592,581 H0 Z" fill="var(--paper)"/>
    <g clip-path="url(#panelClip)">
      <rect x="0" y="158" width="854" height="165" fill="url(#navyBack)"/>
      <path d="M0,458 C170,440 340,445 520,478 V581 H0 Z" fill="var(--navy)"/>
      <path d="M0,470 C170,452 330,456 520,486 V581 H0 Z" fill="var(--white)"/>
    </g>
    <path d="M0,478 C220,458 420,470 592,581 H0 Z" fill="url(#redBack)"/>
    <path d="M380,0 C470,150 520,380 592,581" fill="none" stroke="var(--gold)" stroke-width="8"/>
  </svg>

  <div class="abs brand back-brand">
    <span class="brand-dot"></span>
    <span class="brand-name">Harborline Lending<br>Group, Inc.</span>
  </div>

  <p class="abs message">I am pleased to inform you that an equity based loan is available for your investment property. This no qualifying loan is possible simple due to the equity you have.</p>
  <p class="abs invite">Please call for a quate.<br>You can also email hello@harborline.loan</p>

  <p class="abs fineprint">*loan is subject to confirmation of equity and os for income property, investment property, rental property, business purpose, other conditions and restrictions apply. Please call for complete program requirements and details. Harborline Lending Group, Inc. 1200 Coastal Way Suite 102, Palm Cove CA 92000. Daniel Marsh CA Dept of Real Estate -Real Estate Broker License # 02145590, NMLS # 560713 CA Dept of Real Estate Corporate License # 02270418, NMLS # 418207.</p>

  <div class="abs call-row back-call">
    <span class="call-tag">CALL</span>
    <span class="phone">800-555-0147</span>
  </div>

  <div class="abs stamp-box"></div>
  <div class="abs address-line" style="top:297px"></div>
  <div class="abs address-line" style="top:337px"></div>
  <div class="abs address-line" style="top:374px"></div>
  <div class="abs address-line" style="top:420px"></div>
</section>

</body>
</html>
```